Social Media Post Quote #3 - Native American Organization

- BLOSSOM - must be included
- Protect your community. Protect Your Elders. Stay Vaccinated. must be included
- Attached, company Logo, campaign logos and sample flu social media image. - our audience likes BRIGHT colors.
- Must include image from the United States, representing Land/Nature from one of the following regions, Plains and Woodlands, or Southwest, or Mountains, or Coast.
- must include quote: The well-being of our community’s mind, body, and spirit is sacred.
- One image will be provided three times - incorporating campaign logos - in some fashion
- For inspiration - https://dorvantek.org/ and https://www.pallorbook.com/Dorvantek

```html
<!DOCTYPE html>
<html lang="en">
<head>
<meta charset="utf-8">
<title>Blossom Flu Vaccination Campaign</title>
<link rel="stylesheet" href="https://fonts.googleapis.com/css2?family=Montserrat:wght@700;800&family=Cinzel:wght@500&display=swap">
<style>
  :root {
    --cream: #ece8e1;
    --maroon: #8c1b2e;
    --teal: #56a8b3;
    --brown: #663300;
    --white: #ffffff;
    --sky: #2fa3c1;
    --rock: #b5502b;
    --rock-dark: #7d3a1f;
  }
  * { margin: 0; padding: 0; box-sizing: border-box; }
  html, body { width: 1200px; height: 1200px; overflow: hidden; background: var(--cream); }
  .post { position: relative; width: 1200px; height: 1200px; background: var(--cream); overflow: hidden; }

  .top-band {
    position: absolute; left: 0; top: 0; width: 1200px; height: 160px;
    background: linear-gradient(180deg, var(--maroon) 0%, var(--teal) 100%);
    opacity: .85;
  }

  .landscape {
    position: absolute; left: 0; top: 640px; width: 1200px; height: 560px; z-index: 1;
    background:
      linear-gradient(180deg, var(--cream) 0%, rgba(236,232,225,0) 14%),
      linear-gradient(180deg, var(--sky) 10%, #9fd3df 30%, var(--rock) 45%, var(--rock-dark) 80%, #5d4a2c 100%);
  }

  .title-frame {
    position: absolute; left: 47px; top: 172px; width: 831px; height: 228px; z-index: 2;
    border: 7px solid var(--teal);
  }
  .campaign-name {
    position: absolute; left: 0; right: 0; top: 30px;
    font-family: "Montserrat", sans-serif; font-weight: 800;
    font-size: 134px; line-height: 1; color: var(--brown);
    text-align: center; letter-spacing: 2px;
  }
  .campaign-bar {
    position: absolute; left: 88px; top: 368px; width: 748px; height: 58px; z-index: 3;
    background: var(--teal);
    font-family: "Cinzel", serif; font-weight: 500;
    font-size: 34px; line-height: 58px; color: var(--brown);
    text-align: center; letter-spacing: 1px;
  }

  .org-mark {
    position: absolute; left: 955px; top: 252px; width: 215px; z-index: 2;
    display: flex; align-items: center; gap: 10px;
    font-family: "Montserrat", sans-serif; font-weight: 800;
    font-size: 26px; color: var(--teal); letter-spacing: 1px;
  }
  .org-mark .dot { width: 20px; height: 20px; border-radius: 50%; background: var(--teal); flex: none; }

  .headline {
    position: absolute; left: 47px; top: 483px; z-index: 2;
    font-family: "Montserrat", sans-serif; font-weight: 800;
    font-size: 54px; line-height: 76px; color: var(--maroon);
    letter-spacing: 6px; text-transform: uppercase;
  }

  .quote-band {
    position: absolute; left: 0; top: 980px; width: 1200px; height: 112px; z-index: 2;
    background: rgba(86, 168, 179, .9);
    display: flex; align-items: center; justify-content: center;
    font-family: "Montserrat", sans-serif; font-weight: 700;
    font-size: 32px; line-height: 44px; color: var(--white);
    text-align: center; letter-spacing: 5px; text-transform: uppercase;
  }
</style>
</head>
<body>
<main class="post">
  <div class="top-band" role="img" aria-label="Zigzag chevron pattern fading from maroon to teal"></div>

  <div class="landscape" role="img" aria-label="Photograph of Southwest red rock buttes under a blue sky with white clouds"></div>

  <div class="title-frame">
    <h1 class="campaign-name">BLOSSOM</h1>
  </div>
  <div class="campaign-bar">FLU VACCINATION CAMPAIGN</div>

  <div class="org-mark"><span class="dot"></span><span>DORVANTEK</span></div>

  <p class="headline">Protect your community.<br>Protect your elders.<br>Stay vaccinated.</p>

  <blockquote class="quote-band">The well-being of our community’s mind,<br>body, and spirit is sacred.</blockquote>
</main>
</body>
</html>
```